Sarood Tradeline Web Design

We need Simple but very Elegant Website for Our Middle East Company based in Kuwait, We are not good in describing design but we need simple but elegant and responsive to attract new market and to enable us competing in business

Industry/Entity Type

It Company

```html
<!DOCTYPE html>
<html lang="en">
<head>
<meta charset="utf-8">
<title>Sarood Tradeline</title>
<link rel="stylesheet" href="https://fonts.googleapis.com/css2?family=Roboto:wght@300;400;500;700&display=swap">
<style>
:root{
  --bg:#ffffff;
  --page:#fafafa;
  --ink:#2b2b2b;
  --muted:#8a8a8a;
  --line:#e2e2e2;
  --accent:#c2492a;
  --dark:#262626;
  --darker:#1d1d1d;
  --icon:#d7d7d7;
}
*{box-sizing:border-box;margin:0;padding:0}
html,body{width:1200px;height:1200px;overflow:hidden;background:var(--bg);font-family:'Roboto',sans-serif;color:var(--ink)}
.site{position:absolute;left:383px;top:20px;width:1200px;height:3180px;transform:scale(0.3623);transform-origin:top left;background:var(--page);box-shadow:0 0 60px rgba(0,0,0,.35)}
/* header */
.topbar{height:83px;background:#fff;display:flex;align-items:center;padding:0 90px;border-bottom:1px solid var(--line)}
.brand{display:flex;align-items:center;gap:14px;font-weight:700;font-size:28px;color:var(--ink)}
.brand-mark{width:26px;height:26px;border:3px solid var(--ink)}
.menu{margin-left:auto;display:flex;gap:30px;font-size:13px;color:#666}
.menu a{text-decoration:none;color:inherit;padding:30px 0}
.menu .current{color:var(--ink);font-weight:700;border-bottom:3px solid var(--accent)}
/* hero */
.hero{position:relative;height:443px;background:linear-gradient(180deg,#6d6fc4 0%,#8a7fc9 35%,#6a5f9e 60%,#3b3450 100%);display:flex;flex-direction:column;align-items:center;justify-content:center;color:#fff}
.hero-title{font-size:62px;font-weight:700;letter-spacing:-1px}
.hero-sub{font-size:22px;font-weight:400;margin-top:4px}
.hero-tag{font-size:16px;margin-top:6px}
/* features */
.features{height:134px;background:#fff;display:flex;justify-content:center;gap:70px;padding-top:45px}
.feature{width:275px}
.feature h3{font-size:14px;letter-spacing:2px;font-weight:700;margin:0 0 18px 34px}
.feature p{font-size:11px;line-height:15px;color:#333}
/* intro */
.intro{height:768px;text-align:center;padding-top:112px;border-bottom:2px solid var(--line)}
.intro h2{font-size:29px;letter-spacing:3px;font-weight:500}
.intro p{font-size:11px;color:#555;line-height:19px;margin-top:80px}
.gallery{display:flex;justify-content:center;gap:4px;margin-top:70px}
.gallery div{width:325px;height:258px}
.g1{background:linear-gradient(180deg,#5b8ab8,#8b8a80 60%,#5b5448)}
.g2{background:linear-gradient(135deg,#b9a789,#6f7c8b 50%,#c14d5a)}
.g3{background:linear-gradient(180deg,#e9a77f,#c56d5d 50%,#394052)}
/* about */
.about{height:500px;display:flex;border-bottom:2px solid var(--line)}
.about-text{width:570px;text-align:right;padding:65px 50px 0 100px}
.about-text h2{font-size:26px;letter-spacing:1px;font-weight:500}
.rule{height:1px;background:var(--line);margin:22px 0 34px 120px}
.about-text p{font-size:11px;line-height:19px;color:var(--muted);margin-bottom:10px}
.about-text b{color:var(--accent)}
.team-btn{display:inline-block;margin-top:40px;border:1px solid var(--line);padding:10px 24px;font-size:10px;color:var(--muted);background:#fff}
.points{padding:65px 0 0 60px;width:530px}
.point{display:flex;gap:30px;margin-bottom:42px}
.point-icon{flex:none;width:60px;height:60px;border-radius:50%;background:var(--icon)}
.point h4{font-size:15px;font-weight:700;letter-spacing:1px;margin-bottom:8px}
.point p{font-size:11px;line-height:19px;color:var(--muted)}
.point b{color:var(--accent)}
/* testimonials */
.quotes{height:553px;text-align:center;padding-top:65px}
.quotes h2{font-size:26px;letter-spacing:2px;font-weight:500}
.quotes .rule{width:400px;margin:22px auto 50px}
.quote-grid{display:grid;grid-template-columns:510px 510px;justify-content:center;text-align:left}
.quote{display:flex;gap:20px;padding:0 20px;height:165px}
.quote:nth-child(odd){border-right:1px solid var(--line)}
.avatar{flex:none;width:76px;height:76px;border-radius:50%;background:linear-gradient(#c9b4a4,#6f5a4e)}
.quote p{font-size:11px;line-height:19px;color:var(--muted)}
.quote strong{display:block;font-size:11px;margin-top:12px}
.quote span{font-size:10px;color:var(--muted)}
.quote span em{font-style:normal;color:var(--accent)}
/* help */
.help{position:relative;height:376px;background:linear-gradient(90deg,#5a5651,#cfcac4 30%,#e8e6e2 55%,#6f6a64 85%,#3a3835);text-align:center;color:#fff;padding-top:45px}
.help h2{font-size:27px;letter-spacing:2px;font-weight:500}
.help .lead{font-size:11px;margin-top:8px}
.cards{display:flex;justify-content:center;gap:58px;margin-top:60px}
.card{position:relative;width:290px;height:178px;background:#fff;color:var(--ink);padding:50px 22px 0}
.card-icon{position:absolute;top:-22px;left:50%;margin-left:-24px;width:48px;height:48px;border-radius:50%;background:var(--accent);color:#fff;font-size:20px;font-weight:700;line-height:48px}
.card h3{font-size:15px;letter-spacing:2px;font-weight:700;margin-bottom:14px;color:var(--ink)}
.card p{font-size:11px;line-height:19px;color:#666}
.card a{font-size:11px;color:var(--accent);text-decoration:none}
/* footer */
.footer{height:274px;background:var(--dark);color:#bbb;display:flex;padding:50px 75px 0 0}
.follow{margin-left:520px;text-align:center;font-size:11px;color:#999;width:220px}
.socials{display:flex;gap:14px;justify-content:center;margin-top:18px}
.socials i{width:16px;height:16px;border-radius:50%;background:#fff;display:block}
.hours{margin-left:auto;width:240px;font-size:11px;line-height:19px}
.hours h4{font-size:12px;letter-spacing:1px;color:#999;font-weight:700;margin-bottom:14px}
.hours p{color:#ddd}
.hours b{color:#fff}
.legal{height:49px;background:var(--darker);display:flex;align-items:center;padding:0 80px 0 100px;font-size:10px;color:#aaa}
.legal nav{margin-left:auto;display:flex;gap:30px;font-weight:700;color:#ccc}
</style>
</head>
<body>
<div class="site">
  <header class="topbar">
    <div class="brand"><span class="brand-mark"></span>Sarood Tradeline</div>
    <nav class="menu">
      <a class="current">Home</a><a>About us</a><a>Products</a><a>Industries</a><a>Innovation</a><a>Careers</a><a>News &amp; Media</a>
    </nav>
  </header>

  <section class="hero" role="img" aria-label="City skyline at dusk with illuminated towers">
    <div class="hero-title">Sarood Tradeline</div>
    <div class="hero-sub">Lorem ipsum dolor sit amet.</div>
    <div class="hero-tag">(TAGLINE)</div>
  </section>

  <section class="features">
    <div class="feature"><h3>LOREM IPSUM</h3><p>Lorem ipsum dolor sit amet, consectetur adipiscing elit. Aenean mollis dapibus placerat. Donec accumsan <b>ultrices faucibus</b>. Duis at ex sed.</p></div>
    <div class="feature"><h3>LOREM IPSUM</h3><p>Lorem ipsum dolor sit amet, consectetur adipiscing elit. Aenean mollis dapibus placerat. Donec accumsan <b>ultrices faucibus</b>. Duis at ex sed.</p></div>
    <div class="feature"><h3>LOREM IPSUM</h3><p>Lorem ipsum dolor sit amet, consectetur adipiscing elit. Aenean mollis dapibus placerat. Donec accumsan <b>ultrices faucibus</b>. Duis at ex sed.</p></div>
  </section>

  <section class="intro">
    <h2>NEQUE PORRO QUISQUAM EST QUI DOLOREM IPSUM</h2>
    <p>Lorem ipsum dolor sit amet, consectetur adipiscing elit. Mauris maximus tristique sem, ut condimentum odio aliquet vitae.<br>Nunc eu rutrum justo. Pellentesque habitant morbi tristique senectus et netus et malesuada fames ac turpis egestas. Phasellus cursus condimentum nisl.</p>
    <div class="gallery">
      <div class="g1" role="img" aria-label="Hazy city skyline with curved towers"></div>
      <div class="g2" role="img" aria-label="Aerial view of a cargo port with containers"></div>
      <div class="g3" role="img" aria-label="Industrial refinery at sunset"></div>
    </div>
  </section>

  <section class="about">
    <div class="about-text">
      <h2>ABOUT US</h2>
      <div class="rule"></div>
      <p>Lorem ipsum dolor sit amet, consectetuer <b>adipiscing elit</b>. Aenean commodo ligula eget dolor. Aenean massa.</p>
      <p>Nulla consequat massa quis enim. Donec pede justo, fringilla vel, aliquet nec, vulputate eget, arcu. In enim justo, rhoncus ut, imperdiet a, venenatis vitae, justo. Nullam dictum felis eu pede mollis pretium. Integer tincidunt. Cras dapibus. Vivamus elementum semper nisi. Aenean <b>vulputate</b> eleifend tellus.</p>
      <div class="rule"></div>
      <span class="team-btn">Check out our Team</span>
    </div>
    <div class="points">
      <div class="point"><span class="point-icon"></span><div><h4>CRAFTED WITH LOVE</h4><p>Aenean vulputate eleifend tellus. Aenean leo ligula, porttitor eu, consequat vitae, eleifend ac, enim. Aliquam lorem ante, dapibus in.</p></div></div>
      <div class="point"><span class="point-icon"></span><div><h4>MELODICAL BY NATURE</h4><p>Donec vitae sapien ut libero venenatis faucibus. Nullam quis ante. Etiam sit amet orci eget eros faucibus tincidunt.</p></div></div>
      <div class="point"><span class="point-icon"></span><div><h4>LIGHTNING FAST</h4><p>Donec sodales sagittis magna. Sed consequat, leo eget bibendum sodales, augue velit cursus nunc, quis gravida magna mi a libero.</p></div></div>
      <div class="point"><span class="point-icon"></span><div><h4>FREAKY FLAGS</h4><p>Nullam quis ante. Etiam sit <b>amet orci eget</b> eros faucibus tincidunt. Donec vitae sapien ut libero venenatis faucibus.</p></div></div>
    </div>
  </section>

  <section class="quotes">
    <h2>WHAT OTHERS SAY ABOUT US</h2>
    <div class="rule"></div>
    <div class="quote-grid">
      <div class="quote"><span class="avatar" role="img" aria-label="Portrait of a client"></span><div><p>Nulla consequat massa quis enim. Donec pede justo, fringilla vel, aliquet nec, vulputate eget, arcu. In enim justo, rhoncus ut, imperdiet a, venenatis vitae, justo. Nullam dictum felis eu pede mollis pretium. Integer tincidunt. Cras dapibus.</p><strong>Lena R. Hartley</strong><span>Marketing – <em>Roamly</em></span></div></div>
      <div class="quote"><span class="avatar" role="img" aria-label="Portrait of a client"></span><div><p>In enim justo, rhoncus ut, imperdiet a, venenatis vitae, justo. Nullam dictum felis eu pede mollis pretium. Integer tincidunt. Cras dapibus.</p><strong>Nadia Soren</strong><span>CEO – <em>Pagewell</em></span></div></div>
      <div class="quote"><span class="avatar" role="img" aria-label="Portrait of a client"></span><div><p>Nulla consequat massa quis enim. Donec pede justo, fringilla vel, aliquet nec, vulputate eget, arcu.</p><strong>Omar Qadri</strong><span>Public Relations – <em>Dunefield</em></span></div></div>
      <div class="quote"><span class="avatar" role="img" aria-label="Portrait of a client"></span><div><p>In enim justo, rhoncus ut, imperdiet a, venenatis vitae, justo. Nullam dictum felis eu pede mollis pretium. Integer tincidunt. Cras dapibus.</p><strong>Dr. Faris Hale</strong><span>Dean of Medicine – <em>Hale Labs</em></span></div></div>
    </div>
  </section>

  <section class="help" role="img" aria-label="Blurred office interior background">
    <h2>IN CASE YOU NEED HELP</h2>
    <p class="lead">Here are some ways to contact us</p>
    <div class="cards">
      <div class="card"><span class="card-icon">?</span><h3>PRESALES QUESTION?</h3><p>Lorem ipsum dolor sit amet, consectetuer adipiscing elit. Aenean commodo ligula eget dolor. Aenean massa.</p><a>Learn more</a></div>
      <div class="card"><span class="card-icon">+</span><h3>NEED SUPPORT?</h3><p>Donec quam felis, ultricies nec, pellentesque eu, pretium quis, sem. Nulla consequat massa quis enim.</p><a>Learn more</a></div>
      <div class="card"><span class="card-icon">≡</span><h3>CHECK FORUM</h3><p>Donec pede justo, fringilla vel, aliquet nec, vulputate eget, arcu. In enim justo, venenatis vitae, justo.</p><a>Learn more</a></div>
    </div>
  </section>

  <footer class="footer">
    <div class="follow">FOLLOW US<div class="socials"><i></i><i></i><i></i><i></i><i></i><i></i></div></div>
    <div class="hours">
      <h4>BUSINESS HOURS</h4>
      <p>Our support Hotline is available 24 Hours a day: +965 2210 4837</p>
      <p style="margin-top:10px"><b>Monday-Friday:</b> 9am to 5pm<br><b>Saturday:</b> 10am to 2pm<br><b>Sunday:</b> Closed</p>
    </div>
  </footer>
  <div class="legal">© Copyright
    <nav><span>Home</span><span>About us</span><span>Products</span><span>Industries</span><span>Innovation</span><span>Careers</span><span>News &amp; Media</span></nav>
  </div>
</div>
</body>
</html>
```